Corran Ridge Builders

we are a construction company that provides the following services:
design and build new homes
building renovations
bathroom renovations
builds deck and patio
fencing and gates
retaining walls
concreting
painting
landscaping
we need a company prospectus that says who we are and the services we provide
the last page should be a quote page so we can write a quote on the spot for small jobs , so should feel that he is dealing with professional company
the front page needs to be strong and catchy that makes you want to read the rest of the pages, this will be a book form with 4 to 6 double sided pages
Target Market(s)
home owners
Industry/Entity Type
Construction
Look and feel

```html
<!DOCTYPE html>
<html lang="en">
<head>
<meta charset="UTF-8">
<title>Corran Ridge Builders – Your Quote</title>
<link href="https://fonts.googleapis.com/css2?family=Cinzel:wght@400&display=swap" rel="stylesheet">
<style>
  :root {
    --gold-deep: #a8882a;
    --gold-mid: #b39541;
    --gold-soft: #c3a868;
    --gold-light: #cdb981;
    --gold-pale: #e6dfc7;
    --paper: #ffffff;
  }
  html, body {
    margin: 0;
    padding: 0;
    overflow: hidden;
    background: var(--paper);
  }
  .quote-page {
    position: relative;
    width: 848px;
    height: 1200px;
    background: var(--paper);
    overflow: hidden;
    font-family: "Cinzel", "Times New Roman", serif;
    color: var(--gold-deep);
  }
  .band {
    position: absolute;
    height: 58px;
  }
  .band--top { top: 52px; }
  .band--bottom { top: 1089px; }
  .tone-deep { background: var(--gold-deep); }
  .tone-mid { background: var(--gold-mid); }
  .tone-soft { background: var(--gold-soft); }
  .tone-light { background: var(--gold-light); }
  .tone-pale { background: var(--gold-pale); }

  .quote-title {
    position: absolute;
    left: 51px;
    top: 138px;
    margin: 0;
    font-weight: 400;
    font-size: 50px;
    letter-spacing: 0.5px;
    line-height: 1;
  }
  .work-list {
    position: absolute;
    top: 226px;
    margin: 0;
    padding: 0;
    list-style: none;
  }
  .work-list--left { left: 51px; width: 296px; }
  .work-list--right { left: 501px; width: 296px; }
  .work-item {
    display: flex;
    justify-content: space-between;
    align-items: center;
    height: 41.3px;
    font-size: 24px;
    line-height: 1;
  }
  .checkbox {
    width: 20px;
    height: 20px;
    border: 1.2px solid var(--gold-deep);
    box-sizing: border-box;
  }
  .notes-box {
    position: absolute;
    left: 50px;
    top: 458px;
    width: 747px;
    height: 487px;
    border: 3px solid var(--gold-deep);
    box-sizing: border-box;
  }
  .cost-label {
    position: absolute;
    left: 53px;
    top: 991px;
    font-size: 27px;
    line-height: 1;
  }
  .cost-currency {
    position: absolute;
    left: 569px;
    top: 991px;
    font-size: 27px;
    line-height: 1;
  }
  .cost-field {
    position: absolute;
    left: 595px;
    top: 987px;
    width: 202px;
    height: 40px;
    border: 3px solid var(--gold-deep);
    box-sizing: border-box;
  }
</style>
</head>
<body>
  <main class="quote-page">
    <div class="band band--top tone-light" style="left:0;width:269px"></div>
    <div class="band band--top tone-mid" style="left:283px;width:103px"></div>
    <div class="band band--top tone-deep" style="left:399px;width:272px"></div>
    <div class="band band--top tone-pale" style="left:686px;width:101px"></div>
    <div class="band band--top tone-soft" style="left:801px;width:47px"></div>

    <h1 class="quote-title">Your Quote</h1>

    <ul class="work-list work-list--left">
      <li class="work-item">Type of Work <span class="checkbox"></span></li>
      <li class="work-item">Type of Work <span class="checkbox"></span></li>
      <li class="work-item">Type of Work <span class="checkbox"></span></li>
      <li class="work-item">Type of Work <span class="checkbox"></span></li>
      <li class="work-item">Type of Work <span class="checkbox"></span></li>
    </ul>
    <ul class="work-list work-list--right">
      <li class="work-item">Type of Work <span class="checkbox"></span></li>
      <li class="work-item">Type of Work <span class="checkbox"></span></li>
      <li class="work-item">Type of Work <span class="checkbox"></span></li>
      <li class="work-item">Type of Work <span class="checkbox"></span></li>
      <li class="work-item">Type of Work <span class="checkbox"></span></li>
    </ul>

    <div class="notes-box"></div>

    <div class="cost-label">Estimated Cost</div>
    <div class="cost-currency">$</div>
    <div class="cost-field"></div>

    <div class="band band--bottom tone-deep" style="left:0;width:171px"></div>
    <div class="band band--bottom tone-light" style="left:187px;width:370px"></div>
    <div class="band band--bottom tone-mid" style="left:575px;width:40px"></div>
    <div class="band band--bottom tone-pale" style="left:630px;width:218px"></div>
  </main>
</body>
</html>
```